Create lumora book cover: Step Aside

I need a cover designed for my book
Title is “Step Aside”
Tag line is “ The Venture Horizon Plan“

With the words “ A handbook on how to remove yourself from your company“ somewhere on the page.

Author name “Neil Corbett”

The cover will be used on lumora and paper back and needs to comply with all RVS formatting rules.

Target Market(s)

Small Business owners

Font styles to use
Serif

```html
<!DOCTYPE html>
<html lang="en">
<head>
<meta charset="utf-8">
<title>Step Aside — Neil Corbett</title>
<link href="https://fonts.googleapis.com/css2?family=Archivo:wght@800;900&family=Didact+Gothic&display=swap" rel="stylesheet">
<style>
  :root {
    --spot: #ffffff;
    --haze: #cfcfcf;
    --stage: #6e6e6e;
    --shadow: #2a2a2a;
    --deep: #1e1e1e;
    --title-red: #a8200f;
    --ink: #111111;
    --tag-white: #f4f4f4;
    --tag-grey: #8c8c8c;
    --check-dark: #0d0d0d;
    --check-light: #9a9a9a;
    --subtitle: #e2e2e2;
  }
  * { margin: 0; padding: 0; box-sizing: border-box; }
  html, body {
    width: 750px; height: 1200px; overflow: hidden; background: var(--deep);
  }
  .cover {
    position: relative; width: 750px; height: 1200px; overflow: hidden;
    background:
      radial-gradient(ellipse 330px 500px at 50% 16%, var(--spot) 0%, var(--haze) 30%, rgba(110,110,110,0.6) 62%, rgba(42,42,42,0) 100%),
      radial-gradient(ellipse 420px 140px at 50% 70%, rgba(200,200,200,0.35) 0%, rgba(42,42,42,0) 100%),
      linear-gradient(180deg, var(--stage) 0%, var(--shadow) 55%, var(--deep) 100%);
  }
  .author {
    position: absolute; top: 42px; left: 0; width: 100%;
    text-align: center; font-family: "Didact Gothic", sans-serif;
    font-size: 54px; line-height: 64px; color: var(--ink); letter-spacing: 1px;
  }
  .title {
    font-family: "Archivo", sans-serif; font-weight: 900; color: var(--title-red);
    text-transform: uppercase;
  }
  .title-line {
    position: absolute; left: 0; width: 100%; text-align: center;
    display: block; line-height: 1;
  }
  .title-line--first { top: 197px; font-size: 180px; letter-spacing: 2px; }
  .title-line--second { top: 364px; font-size: 140px; letter-spacing: 1px; }
  .tagline {
    position: absolute; top: 540px; left: 0; width: 100%;
    font-family: "Archivo", sans-serif; font-weight: 800; text-transform: uppercase;
    text-align: center;
  }
  .tag-row {
    display: flex; align-items: center; justify-content: center; gap: 20px; height: 40px;
  }
  .tag-row + .tag-row { margin-top: 22px; }
  .tag-word { font-size: 48px; line-height: 40px; }
  .tag-word--lead { color: var(--tag-white); }
  .tag-word--main { color: var(--tag-grey); font-size: 46px; letter-spacing: 1px; }
  .checker { display: block; }
  .finish-line {
    position: absolute; top: 760px; left: 40px; width: 670px; height: 150px;
    background: radial-gradient(ellipse at 50% 50%, rgba(210,210,210,0.45) 0%, rgba(140,140,140,0.2) 50%, rgba(42,42,42,0) 75%);
  }
  .subtitle {
    position: absolute; top: 922px; left: 0; width: 100%; text-align: center;
    font-family: "Didact Gothic", sans-serif; font-size: 51px; line-height: 72px;
    color: var(--subtitle);
  }
</style>
</head>
<body>
<main class="cover">
  <p class="author">NEIL<br>CORBETT</p>

  <h1 class="title">
    <span class="title-line title-line--first">Step</span>
    <span class="title-line title-line--second">Aside</span>
  </h1>

  <div class="tagline">
    <div class="tag-row">
      <svg class="checker" width="190" height="36" viewBox="0 0 190 36" aria-hidden="true">
        <rect x="0" y="0" width="190" height="36" fill="var(--check-light)"/>
        <rect x="0" y="0" width="38" height="36" fill="var(--check-dark)"/>
        <rect x="76" y="0" width="38" height="36" fill="var(--check-dark)"/>
        <rect x="152" y="0" width="38" height="36" fill="var(--check-dark)"/>
      </svg>
      <span class="tag-word tag-word--lead">The</span>
      <svg class="checker" width="190" height="36" viewBox="0 0 190 36" aria-hidden="true">
        <rect x="0" y="0" width="190" height="36" fill="var(--check-light)"/>
        <rect x="0" y="0" width="38" height="36" fill="var(--check-dark)"/>
        <rect x="76" y="0" width="38" height="36" fill="var(--check-dark)"/>
        <rect x="152" y="0" width="38" height="36" fill="var(--check-dark)"/>
      </svg>
    </div>
    <div class="tag-row">
      <span class="tag-word tag-word--main">Venture Horizon</span>
    </div>
    <div class="tag-row">
      <svg class="checker" width="114" height="36" viewBox="0 0 114 36" aria-hidden="true">
        <rect x="0" y="0" width="114" height="36" fill="var(--check-light)"/>
        <rect x="0" y="0" width="38" height="36" fill="var(--check-dark)"/>
        <rect x="76" y="0" width="38" height="36" fill="var(--check-dark)"/>
      </svg>
      <span class="tag-word tag-word--main">Plan</span>
      <svg class="checker" width="114" height="36" viewBox="0 0 114 36" aria-hidden="true">
        <rect x="0" y="0" width="114" height="36" fill="var(--check-light)"/>
        <rect x="0" y="0" width="38" height="36" fill="var(--check-dark)"/>
        <rect x="76" y="0" width="38" height="36" fill="var(--check-dark)"/>
      </svg>
    </div>
  </div>

  <div class="finish-line" role="img" aria-label="Two crossed checkered racing flags lying on a spotlit floor"></div>

  <p class="subtitle">A handbook on how to<br>remove yourself from<br>your company</p>
</main>
</body>
</html>
```